Design Website Templates for Photographers for Lumora Inc. (trywendle.com)

Lumora Inc. is a generative website company for wedding photographers.
We are seeking new photography website design inspirations for the next template to be offered on our platform. The catch is you must use the same data for your designs. You also must use all of the data somewhere in the design. You cannot add new content besides the data available. If you wish to add any elements It will be hardcoded and must be universally fitting for many different photographers. We recommend not using any hardcoded test.
Don't be afraid to be creative! Although the most important element of a photographers website is the photos, we are looking for unique and out-of-the-box designs for the actual site as well.
Here is the User generated data available to you:
- 4 Hero Images Landscape, 4 Hero Images Portrait
- Tagline “destination photographer based in Maui, Hawaii”
- “About Photo” of the photographer
- “About” Biography Text
- The design can use up to 3 colors + background color and 2 fonts
- 9 Gallery images
- 3 Packages/services that include landscape/portrait images, a price, a title and text
- Testimonials made up of an image, text and text for the name of testimonial giver
See some examples of our current website designs attached. You can use any of the data you see in the designs.
Updates
We are looking for designs that are less feminine and are more neutral in color and fonts. Currently our templates are more oriented towards feminine photographers. We want to have designs that speak to diverse audiences. We thank everyone for submitting and are reviewing the designs.
Number of Pages Required
1 page
Look and feel
Each slider illustrates characteristics of the customer's brand and the style your logo design should communicate.

```html
<!DOCTYPE html>
<html lang="en">
<head>
<meta charset="utf-8">
<title>Ren Photography</title>
<link href="https://fonts.googleapis.com/css2?family=Roboto:wght@300;400;500&family=Courgette&display=swap" rel="stylesheet">
<style>
:root{
  --ink:#111111;
  --panel:#000000;
  --white:#ffffff;
  --soft:#d8d6d2;
  --muted:#3b3a38;
  --taupe:#6f6b64;
  --deep:#3e3d3a;
  --paper:#f6f6f5;
  --button:#4a4947;
}
*{box-sizing:border-box;margin:0;padding:0}
html,body{width:1200px;height:4777px;overflow:hidden}
body{
  font-family:"Roboto",Arial,sans-serif;
  color:var(--white);
  background:linear-gradient(180deg,var(--ink) 0,var(--ink) 556px,#7a766e 560px,#5b5853 1000px,var(--deep) 1350px,#474642 2250px,#8f8b85 3000px,#d9d7d3 3230px,var(--paper) 3380px,var(--paper) 100%);
}
.page{position:relative;width:1200px;height:4777px}
.abs{position:absolute}
.photo{position:absolute;display:block}
a{color:inherit}
.script{font-family:"Courgette",cursive;font-weight:400}

/* hero */
.hero{left:0;top:0;width:1200px;height:556px;background:radial-gradient(ellipse 150px 230px at 600px 340px,#c9c4bb 0,#7a6f62 35%,#2a2320 70%,#0d0b0a 100%)}
.hero-side-left{left:0;top:180px;width:120px;height:280px;background:linear-gradient(90deg,#3a1e14,#7a3c28);opacity:.8}
.hero-side-right{left:1070px;top:180px;width:130px;height:280px;background:linear-gradient(270deg,#3a1e14,#7a3c28);opacity:.8}
.book-btn{left:959px;top:20px;width:106px;height:27px;border:1px solid var(--white);font-size:11px;line-height:25px;text-align:center}
.menu{left:1110px;top:25px}
.hero-arrow{top:205px}
.brand-hero{left:38px;top:478px;width:130px;font-size:17px;line-height:20px;color:var(--white)}
.hero-dots{top:516px;width:78px;height:78px;border-radius:50%;border:2px solid #ffffff66}

/* about */
.about-photo{left:83px;top:723px;width:301px;height:346px;background:linear-gradient(180deg,#3a3f44 0,#5d6066 45%,#8a6a4a 80%,#3a2a20 100%)}
.aloha{left:482px;top:728px;font-size:44px;letter-spacing:1px}
.tagline{left:486px;top:792px;font-size:16px;font-weight:300;text-decoration:underline}
.bio{left:483px;width:446px;font-size:10.5px;line-height:16px;font-weight:300;color:#e8e6e2}
.contact-btn{left:480px;top:1057px;width:155px;height:37px;border:1px solid var(--white);font-size:16px;font-weight:300;line-height:35px;text-align:center}

/* sections */
.section-title{left:0;width:1232px;text-align:center;font-size:36px}
.label{left:57px;font-size:21px;font-weight:300;text-decoration:underline}
.more{font-size:15px;font-weight:300;display:flex;align-items:center;gap:8px}
.more span{text-decoration:underline}

.album-panel{left:599px;top:1697px;width:540px;height:113px;background:var(--panel);padding:30px 24px}
.album-panel h3{font-size:18px;font-weight:400;margin-bottom:12px}
.album-panel p{font-size:9.5px;line-height:13px;font-weight:300;width:330px}

.thumb{top:2371px;width:180px;height:91px}

/* packages */
.pkg-panel{left:391px;top:3363px;width:368px;height:468px;background:var(--panel);padding:68px 52px 0 71px}
.pkg-panel h3{font-size:22px;font-weight:400;margin-bottom:30px}
.pkg-panel p{font-size:12px;line-height:19px;font-weight:300}
.price{left:532px;top:3643px;width:119px;height:33px;border:1px solid var(--white);font-size:16px;font-weight:300;line-height:31px;text-align:center}
.details{left:627px;top:3779px;font-size:10px}
.circle-btn{width:56px;height:56px;border-radius:50%;display:flex;align-items:center;justify-content:center}
.dark-btn{background:#3c3c3c;border:2px solid var(--white)}
.light-btn{background:var(--white);border:1px solid #bdbdbd}
.dots{display:flex;gap:4px}
.dots i{width:11px;height:11px;border-radius:50%;background:#c8c8c8;display:block}
.dots i:first-child{background:#8a8a8a}
.touch-btn{left:523px;top:3916px;width:152px;height:38px;background:var(--button);font-size:16px;line-height:38px;text-align:center}

/* testimonials */
.quote-panel{top:4048px;width:266px;height:349px;background:var(--panel);padding:34px 22px 0 26px}
.avatar-row{display:flex;align-items:center;gap:8px;margin-bottom:14px}
.avatar{width:40px;height:40px;border-radius:50%;background:linear-gradient(135deg,#d9c7b8,#6a5548)}
.avatar-row span{font-size:14px;text-decoration:underline}
.quote-panel p{font-size:9px;line-height:13.5px;font-weight:300;color:#dcdcdc;padding:0 4px}
.qmark{font-family:Georgia,serif;font-size:18px;color:#cfcfcf}

/* footer */
.footer-note{left:95px;top:4630px;font-size:16px;font-weight:300;color:var(--muted);text-decoration:underline}
.social{top:4680px;width:20px;height:20px;border-radius:50%;background:#1d1d1d}
.brand-footer{left:460px;top:4612px;width:280px;text-align:center;font-size:40px;line-height:44px;font-weight:300;color:var(--muted)}
.footer-links{left:989px;top:4638px;font-size:12px;color:#3d4f7a;display:flex;gap:8px}
.footer-links a{text-decoration:underline}
</style>
</head>
<body>
<div class="page">

  <header>
    <div class="abs hero photo" role="img" aria-label="Couple in silhouette holding hands beneath a stone archway, glowing sky behind them"></div>
    <div class="abs hero-side-left photo" role="img" aria-label="Warm-lit stone column on the left"></div>
    <div class="abs hero-side-right photo" role="img" aria-label="Warm-lit stone column on the right"></div>
    <a class="abs book-btn">Book with me</a>
    <svg class="abs menu" width="26" height="20" viewBox="0 0 26 20" aria-label="Menu"><g stroke="#ffffff" stroke-width="1.5"><line x1="0" y1="2" x2="26" y2="2"/><line x1="0" y1="10" x2="26" y2="10"/><line x1="0" y1="18" x2="26" y2="18"/></g></svg>
    <svg class="abs hero-arrow" style="left:58px" width="34" height="66" viewBox="0 0 34 66" aria-label="Previous"><polyline points="32,2 2,33 32,64" fill="none" stroke="#ffffff" stroke-width="2"/></svg>
    <svg class="abs hero-arrow" style="left:1108px" width="34" height="66" viewBox="0 0 34 66" aria-label="Next"><polyline points="2,2 32,33 2,64" fill="none" stroke="#ffffff" stroke-width="2"/></svg>
    <div class="abs brand-hero">Ren<br>Photography</div>
    <div class="abs hero-dots photo" style="left:427px;background:linear-gradient(180deg,#9fb6c8,#4e6a80)" role="img" aria-label="Coastal landscape preview"></div>
    <div class="abs hero-dots photo" style="left:519px;background:linear-gradient(180deg,#a0593f,#3a1c18)" role="img" aria-label="Warm sunset preview"></div>
    <div class="abs hero-dots photo" style="left:607px;background:linear-gradient(180deg,#6f8fa6,#3c5a48)" role="img" aria-label="Green cliffs and sea preview"></div>
    <div class="abs hero-dots photo" style="left:692px;background:linear-gradient(180deg,#cfd6dc,#7f8b94)" role="img" aria-label="Misty beach preview"></div>
  </header>

  <section class="about">
    <svg class="abs" style="left:59px;top:701px" width="68" height="68" viewBox="0 0 68 68"><polyline points="2,68 2,2 68,2" fill="none" stroke="#ffffff" stroke-width="3"/></svg>
    <div class="about-photo photo" role="img" aria-label="Photographer crouching on a palm-lined road holding a camera"></div>
    <svg class="abs" style="left:341px;top:1026px" width="68" height="68" viewBox="0 0 68 68"><polyline points="0,66 66,66 66,0" fill="none" stroke="#ffffff" stroke-width="3"/></svg>
    <h1 class="abs aloha script">ALOHA!!</h1>
    <p class="abs tagline">I am Ren, a destination photographer based in Maui, Hawaii</p>
    <p class="abs bio" style="top:856px">Lorem ipsum dolor sit amet consectetur. Libero purus eget commodo varius sit leo quis neque viverra. Et velit venenatis duis velit amet turpis. Gravida odio nec sed ultrices ornare justo. In sit tristique purus sed hac erat commodo quam.</p>
    <p class="abs bio" style="top:920px">Pharetra pharetra sed etiam placerat est non sem pellentesque sit. Sodales semper eu consectetur enim cursus dignissim. Nibh malesuada consequat velit iaculis lacus vitae in etiam ac. Sed viverra ipsum sed tellus posuere facilisis. Dui velit suspendisse id mattis risus libero vitae cras. Nisi ut sed duis morbi lacus nunc eu quam.</p>
    <a class="abs contact-btn">Contact me !</a>
  </section>

  <section class="latest">
    <h2 class="abs section-title script" style="top:1198px">Latest Work</h2>

    <a class="abs label" style="top:1282px">Albums</a>
    <div class="photo" style="left:57px;top:1330px;width:542px;height:480px;background:linear-gradient(160deg,#e6d6bf 0,#c8a784 50%,#8f6b4a 100%)" role="img" aria-label="Laughing couple walking hand in hand through the surf"></div>
    <div class="photo" style="left:599px;top:1330px;width:270px;height:184px;background:linear-gradient(180deg,#9bb4c2,#3f5c6a 60%,#2a3136)" role="img" aria-label="Two surfers walking into the waves"></div>
    <div class="photo" style="left:869px;top:1330px;width:270px;height:184px;background:linear-gradient(180deg,#f0c895,#a9b4b8 60%,#6c8a96)" role="img" aria-label="Woman in white dress on the shoreline"></div>
    <div class="photo" style="left:599px;top:1514px;width:270px;height:183px;background:linear-gradient(180deg,#1fa9c9,#0a6c8e)" role="img" aria-label="Swimmer underwater in turquoise sea"></div>
    <div class="photo" style="left:869px;top:1514px;width:270px;height:183px;background:linear-gradient(180deg,#8b98a4,#c9b39a 70%,#6e5c4c)" role="img" aria-label="Couple holding hands by the sea"></div>
    <div class="abs album-panel">
      <h3>Beach Album</h3>
      <p>Lorem ipsum dolor sit amet consectetur. Facilisi mattis cursus vitae mauris erat malesuada sed sem duis. Erat sed id amet nibh eget.</p>
    </div>
    <a class="abs more" style="left:1037px;top:1840px"><span>View all</span><svg width="24" height="10" viewBox="0 0 24 10"><g fill="none" stroke="#ffffff" stroke-width="1.4"><line x1="0" y1="5" x2="22" y2="5"/><polyline points="17,1 22,5 17,9"/></g></svg></a>

    <a class="abs label" style="top:1927px">Wedding</a>
    <div class="photo" style="left:61px;top:1976px;width:1078px;height:384px;background:linear-gradient(100deg,#2a2522 0,#4a3f38 30%,#cbb6a4 55%,#2b2d35 80%,#1d1e22 100%)" role="img" aria-label="Close-up of bride and groom holding hands, lace sleeve and wedding ring"></div>
    <div class="abs thumb photo" style="left:61px;background:linear-gradient(180deg,#6c7a6a,#4a4038)" role="img" aria-label="Wedding party dancing"></div>
    <div class="abs thumb photo" style="left:245px;background:linear-gradient(180deg,#b39a7c,#6d5a42)" role="img" aria-label="Couple embracing among flowers"></div>
    <div class="abs thumb photo" style="left:429px;background:linear-gradient(180deg,#d2c7a5,#4c5a3c)" role="img" aria-label="Couple in a field at sunset"></div>
    <div class="abs thumb photo" style="left:613px;background:linear-gradient(180deg,#2a2a2a,#cfcac2 60%,#3a3a3a)" role="img" aria-label="Bride walking in a hallway"></div>
    <div class="abs thumb photo" style="left:797px;background:linear-gradient(180deg,#f2d3b2,#c58d66)" role="img" aria-label="Couple at golden hour"></div>
    <div class="abs thumb photo" style="left:981px;width:96px;background:linear-gradient(90deg,#f1d6bb,#6a4a33)" role="img" aria-label="Bride in warm light"></div>
    <svg class="abs" style="left:1086px;top:2398px" width="18" height="36" viewBox="0 0 18 36" aria-label="Next"><polyline points="2,2 16,18 2,34" fill="none" stroke="#ffffff" stroke-width="1.6"/></svg>
    <a class="abs more" style="left:1030px;top:2494px"><span>Gallery</span><svg width="24" height="10" viewBox="0 0 24 10"><g fill="none" stroke="#ffffff" stroke-width="1.4"><line x1="0" y1="5" x2="22" y2="5"/><polyline points="17,1 22,5 17,9"/></g></svg></a>

    <a class="abs label" style="top:2581px;left:60px">Portrait</a>
    <div class="photo" style="left:61px;top:2629px;width:353px;height:482px;background:linear-gradient(135deg,#7b3a6a 0,#3f5a5c 50%,#b4b6b8 100%)" role="img" aria-label="Portrait of a woman in profile with braided hair under teal and magenta light"></div>
    <div class="photo" style="left:419px;top:2629px;width:358px;height:482px;background:linear-gradient(180deg,#6e4a40 0,#c9a493 40%,#a99a8c 100%)" role="img" aria-label="Portrait of a woman wearing a brown cap"></div>
    <div class="photo" style="left:781px;top:2629px;width:358px;height:482px;background:linear-gradient(180deg,#2d3a2a 0,#4d5a48 45%,#5d5f63 100%)" role="img" aria-label="Portrait of a woman in a black hat among green leaves"></div>
    <a class="abs more" style="left:1026px;top:3145px;color:#5a5855"><span>Explore</span><svg width="24" height="10" viewBox="0 0 24 10"><g fill="none" stroke="#5a5855" stroke-width="1.4"><line x1="0" y1="5" x2="22" y2="5"/><polyline points="17,1 22,5 17,9"/></g></svg></a>
  </section>

  <section class="packages">
    <h2 class="abs section-title script" style="top:3281px;width:1210px;color:var(--muted)">Recent packages</h2>
    <div class="photo" style="left:43px;top:3363px;width:348px;height:468px;background:linear-gradient(180deg,#b77a4a 0,#6a3f26 60%,#3a2316 100%)" role="img" aria-label="Portrait of a woman resting her chin on her hands"></div>
    <div class="abs pkg-panel">
      <h3>Portrait Collection</h3>
      <p>Lorem ipsum dolor sit amet consectetur. Tortor turpis urna risus in eros nunc in sem. Sit viverra est massa pretium amet tristique. Enim feugiat est eget</p>
    </div>
    <div class="abs price">1000 $</div>
    <a class="abs details more" style="font-size:10px"><span>more details</span><svg width="20" height="10" viewBox="0 0 20 10"><g fill="none" stroke="#ffffff" stroke-width="1.3"><line x1="0" y1="5" x2="18" y2="5"/><polyline points="13,1 18,5 13,9"/></g></svg></a>
    <div class="photo" style="left:774px;top:3363px;width:350px;height:468px;background:linear-gradient(90deg,#d7dadd,#8f96a0 60%,#aab0b6)" role="img" aria-label="Bride and groom holding hands, faded"></div>
    <div class="photo" style="left:1124px;top:3363px;width:76px;height:468px;background:#8a8a8a"></div>
    <div class="abs circle-btn dark-btn" style="left:15px;top:3570px"><svg width="24" height="20" viewBox="0 0 24 20"><g fill="none" stroke="#ffffff" stroke-width="1.6"><line x1="2" y1="10" x2="22" y2="10"/><polyline points="10,2 2,10 10,18"/></g></svg></div>
    <div class="abs circle-btn dark-btn" style="left:1127px;top:3570px"><svg width="24" height="20" viewBox="0 0 24 20"><g fill="none" stroke="#ffffff" stroke-width="1.6"><line x1="2" y1="10" x2="22" y2="10"/><polyline points="14,2 22,10 14,18"/></g></svg></div>
    <div class="abs dots" style="left:575px;top:3856px"><i></i><i></i><i></i></div>
    <a class="abs touch-btn">Get it touch !</a>
  </section>

  <section class="testimonials">
    <div class="photo" style="left:61px;top:4048px;width:265px;height:349px;background:linear-gradient(180deg,#8a6a48 0,#c49a6c 45%,#6b5340 100%)" role="img" aria-label="Couple kissing on a sandy beach"></div>
    <div class="abs quote-panel" style="left:326px">
      <div class="avatar-row"><div class="avatar" role="img" aria-label="Client photo"></div><span>Lena Ward</span></div>
      <div class="qmark">&ldquo;</div>
      <p>Lorem ipsum dolor sit amet consectetur. Quisque at lorem viverra sit augue risus non porttitor. Egestas aenean est nec amet aenean sit egestas sed. Enim ultrices pretium convallis habitant dignissim ipsum nunc. Duis ut tempus ac urna ipsum curabitur. Habitant quis morbi vulputate mattis adipiscing. Imperdiet purus vitae sed ut erat ut.</p>
      <div class="qmark" style="text-align:right">&rdquo;</div>
    </div>
    <div class="photo" style="left:608px;top:4048px;width:266px;height:349px;background:linear-gradient(180deg,#d5e2ea 0,#b9cbd6 55%,#a98e74 100%)" role="img" aria-label="Man carrying a woman on his shoulders on the beach"></div>
    <div class="abs quote-panel" style="left:874px;width:267px">
      <div class="avatar-row"><div class="avatar" role="img" aria-label="Client photo"></div><span>Mark Delo</span></div>
      <div class="qmark">&ldquo;</div>
      <p>Lorem ipsum dolor sit amet consectetur. Quisque at lorem viverra sit augue risus non porttitor. Egestas aenean est nec amet aenean sit egestas sed. Enim ultrices pretium convallis habitant dignissim ipsum nunc. Duis ut tempus ac urna ipsum curabitur. Habitant quis morbi vulputate mattis adipiscing. Imperdiet purus vitae sed ut erat ut.</p>
      <div class="qmark" style="text-align:right">&rdquo;</div>
    </div>
    <div class="abs circle-btn light-btn" style="left:34px;top:4194px"><svg width="24" height="20" viewBox="0 0 24 20"><g fill="none" stroke="#333333" stroke-width="1.6"><line x1="2" y1="10" x2="22" y2="10"/><polyline points="10,2 2,10 10,18"/></g></svg></div>
    <div class="abs circle-btn light-btn" style="left:1110px;top:4194px"><svg width="24" height="20" viewBox="0 0 24 20"><g fill="none" stroke="#333333" stroke-width="1.6"><line x1="2" y1="10" x2="22" y2="10"/><polyline points="14,2 22,10 14,18"/></g></svg></div>
    <div class="abs dots" style="left:575px;top:4424px"><i></i><i></i><i></i></div>
  </section>

  <footer>
    <a class="abs footer-note">Check my pages for more!</a>
    <a class="abs social" style="left:150px" aria-label="Social page one"></a>
    <a class="abs social" style="left:183px" aria-label="Social page two"></a>
    <a class="abs social" style="left:216px" aria-label="Social page three"></a>
    <div class="abs brand-footer">Ren<br><span style="font-size:34px">Photography</span></div>
    <nav class="abs footer-links"><a>Portfolio</a><span>|</span><a>Get in touch</a></nav>
  </footer>

</div>
</body>
</html>
```